【 概要 】 会計事務所・行政書士事務所共用のお客様用駐車場の案内看板のデザインをお願いします。 設置場所は高さ1.3メートルくらいの駐車場のフェンスです。(看板 仕上がりサイズ横360センチ× 縦90センチ) 設置場所の写真を添付しました。 【 依頼内容 】 ・デザインサイズ:横180センチ× 縦45センチ(解像度300dpi) (仕上がりのサイズは横360センチ×縦90センチです) ・ロゴの用意(画像・文章等):添付ファイルご参照ください。 ・ 【デザイン内容】 以下の情報の掲載をお願いします 〇事務所名:松ヶ枝経営会計事務所、フェリオン行政書士法人 〇駐車場の案内文:P お客様駐車場、駐車番号(⑪ ⑫ ⑬ ⑭ ⑮) 〇会社ロゴ:2社 〇文字:夜間や雨天時でも読みやすい大きくはっきりとした字体でお願いします 〇イメージカラー:松ヶ枝会計:青 フェリオン行政書士法人:赤 〇使用色数:3~4色でお願いします(希望する色を「青」としましたが、他の色でも構いません) 【 デザインイメージ 】 ・ターゲット層:都心在住 ビジネスマン ・雰囲気:落ち着きのある雰囲気 【設置場所】 ・住所:名古屋市東栄区鶴見台町82番地 ビル裏の駐車場 ・GoogleマップスURL:https://maps.example-map.test/Qx7LtRwe2KdNpHa4M ・事務所HP:松ヶ枝経営会計事務所 https://www.matsugaekaikei-sample.net/ フェリオン行政書士法人 https://office-ferion-sample.com/ 【 契約金額(税抜) 】 5.5万円 ※契約金額(税込)からシステム利用料を差し引いた金額が、ワーカーさまの受取金額となります その他ご質問等ありましたら、気軽にお問い合わせください。 ご応募をお待ちしております! |
どの作品も素敵でしたが、kurumiyu.様の作品が最もイメージに合っていました。ありがとうございました。
皆様、数々のご提案誠にありがとうございました。どちらの作品も依頼内容を読み込んでいただき、みなさまのお考えが反映されておりました。
また機会がありましたら、依頼させて頂きますので宜しくお願い致します。

```html
<!DOCTYPE html>
<html lang="ja">
<head>
<meta charset="UTF-8">
<title>お客様駐車場 案内看板</title>
<link rel="stylesheet" href="https://fonts.googleapis.com/css2?family=Noto+Sans+JP:wght@500;700;900&display=swap">
<style>
  :root {
    --brand-blue: #2b5fbf;
    --brand-red: #d8232a;
    --sign-white: #ffffff;
    --ink-dark: #222222;
    --page-bg: #eeeeee;
    --rule-grey: #c9c9c9;
  }
  * { margin: 0; padding: 0; box-sizing: border-box; }
  html, body {
    width: 1200px;
    height: 994px;
    overflow: hidden;
    background: var(--page-bg);
    font-family: "Noto Sans JP", sans-serif;
  }
  .signboard {
    position: absolute;
    left: 40px;
    top: 357px;
    width: 1120px;
    height: 280px;
    background: var(--sign-white);
    border: 1px solid var(--rule-grey);
  }
  .sign-title {
    position: absolute;
    left: 28px;
    top: 22px;
    color: var(--brand-blue);
    font-weight: 900;
    font-size: 104px;
    line-height: 114px;
    letter-spacing: -2px;
  }
  .office-names {
    position: absolute;
    left: 392px;
    top: 34px;
    width: 470px;
    display: flex;
    justify-content: space-between;
    align-items: flex-end;
  }
  .office {
    display: flex;
    flex-direction: column;
    align-items: center;
    gap: 12px;
  }
  .office-mark {
    width: 52px;
    height: 52px;
  }
  .office--admin .office-mark { background: var(--brand-red); }
  .office--accounting .office-mark { background: var(--brand-blue); }
  .office-name {
    font-weight: 700;
    font-size: 21px;
    color: var(--ink-dark);
    white-space: nowrap;
    padding-top: 6px;
    border-top: 2px solid var(--rule-grey);
  }
  .space-numbers {
    position: absolute;
    left: 392px;
    top: 172px;
    display: flex;
    align-items: center;
    gap: 12px;
  }
  .space-label {
    width: 66px;
    height: 66px;
    background: var(--brand-red);
    color: var(--sign-white);
    font-weight: 900;
    font-size: 25px;
    line-height: 29px;
    text-align: center;
    border-radius: 6px;
    padding-top: 4px;
  }
  .space-number {
    width: 66px;
    height: 66px;
    border-radius: 50%;
    background: var(--brand-red);
    color: var(--sign-white);
    font-weight: 900;
    font-size: 36px;
    display: flex;
    align-items: center;
    justify-content: center;
    letter-spacing: -2px;
  }
  .parking-symbol {
    position: absolute;
    right: 36px;
    top: 30px;
    width: 220px;
    height: 220px;
  }
</style>
</head>
<body>
  <main class="signboard">
    <h1 class="sign-title">お客様<br>駐車場</h1>

    <div class="office-names">
      <div class="office office--admin">
        <span class="office-mark"></span>
        <span class="office-name">フェリオン行政書士法人</span>
      </div>
      <div class="office office--accounting">
        <span class="office-mark"></span>
        <span class="office-name">松ヶ枝経営会計事務所</span>
      </div>
    </div>

    <div class="space-numbers">
      <div class="space-label">駐車<br>番号</div>
      <span class="space-number">11</span>
      <span class="space-number">12</span>
      <span class="space-number">13</span>
      <span class="space-number">14</span>
      <span class="space-number">15</span>
    </div>

    <svg class="parking-symbol" viewBox="0 0 220 220" role="img" aria-label="駐車場マーク P">
      <rect x="0" y="0" width="220" height="220" rx="24" fill="var(--brand-blue)"/>
      <path d="M70 40 H125 A45 45 0 0 1 125 130 H98 V180 H70 Z M98 64 V106 H122 A21 21 0 0 0 122 64 Z" fill="var(--sign-white)" fill-rule="evenodd"/>
    </svg>
  </main>
</body>
</html>
```